Accident Law Firm Billboard Bold Easy to See Car Accidents

We need a billboard design that can catch attention in a very crowed Car Accident lawyer market. We wish to feature the phone number (407) 555-0148 as the focus of the Bill Board. We are trying to get the phone number recognized and remembered by drivers. The law firm name is not as crucial to remember.
Basically, It's CAR ACCIDENT? Then (407) 555-0148. We are not married to any specific color scheme but it has to POP and catch attention.
So the Crucial elements are as follows:
1. Phone number (407) 555-0148
2. Words CAR ACCIDENT?
3. Firm Logo in lower portion or where appropriate. Firm Logo to be provided
4. We may want to try a Day Glow orange color, with White and Black added. An example of the color scheme shall be provided.
5. Possible "Catch Phrase" to be used, "Don't Wait Call Now"
Target Market(s)
Orlando Florida Car Accident victims
Industry/Entity Type
Law Firm
Requirements
Must have
- Easy to see phone number (407) 555-0148
- Catch attention
Nice to have
- I would like to have the sign visible in bright sunlight and it not too hard to immediately know what phone number is for
Should not have
- too many words
- No bold enough
- confusing fonts
- Unclear fonts

```html
<!DOCTYPE html>
<html lang="en">
<head>
<meta charset="utf-8">
<title>Marcona Law Firm – Car Accident Billboard</title>
<link rel="stylesheet" href="https://fonts.googleapis.com/css2?family=Archivo+Black&family=Archivo:wght@500;700&display=swap">
<style>
  :root {
    --page: #ece7df;
    --board-black: #1f1f1f;
    --orange: #ff4d12;
    --white: #ffffff;
  }
  * { margin: 0; padding: 0; box-sizing: border-box; }
  html, body {
    width: 752px; height: 1200px; overflow: hidden;
    background: var(--page);
  }
  .billboard {
    position: absolute;
    left: 26px; top: 366px;
    width: 700px; height: 467px;
    background: var(--board-black);
    overflow: hidden;
    box-shadow: 0 10px 24px rgba(0,0,0,.35);
  }
  .billboard__banner {
    position: absolute; left: 0; top: 0;
    width: 700px; height: 230px;
  }
  .firm-name {
    position: absolute; left: 0; right: 0; top: 30px;
    text-align: center;
    color: var(--white);
    font-family: "Archivo", sans-serif;
    font-weight: 700;
    line-height: 1;
  }
  .firm-name__main { display: block; font-size: 30px; letter-spacing: 1px; }
  .firm-name__sub { display: block; font-size: 15px; letter-spacing: 4px; margin-top: 2px; }
  .headline {
    position: absolute; left: 0; right: 0; top: 88px;
    text-align: center;
    color: var(--white);
    font-family: "Archivo Black", sans-serif;
    font-size: 64px;
    line-height: 1.2;
    letter-spacing: 1px;
    text-shadow: 2px 3px 0 rgba(0,0,0,.35);
  }
  .phone {
    position: absolute; left: 34px; top: 256px;
    display: flex; align-items: center; gap: 14px;
  }
  .phone__icon { width: 62px; height: 62px; flex: none; }
  .phone__number {
    font-family: "Archivo Black", sans-serif;
    font-size: 66px;
    line-height: 1.1;
    color: var(--orange);
    white-space: nowrap;
    text-shadow: 2px 2px 0 rgba(255,255,255,.25);
  }
  .slogan {
    position: absolute; right: 40px; top: 354px;
    display: flex; height: 63px;
    border: 2px solid var(--white);
    font-family: "Archivo", sans-serif;
    font-weight: 700;
    font-size: 36px;
    color: var(--white);
    white-space: nowrap;
  }
  .slogan__lead {
    display: flex; align-items: center; padding: 0 14px;
    background: var(--board-black);
  }
  .slogan__action {
    display: flex; align-items: center; padding: 0 14px;
    background: var(--orange);
  }
</style>
</head>
<body>
  <main class="billboard">
    <svg class="billboard__banner" viewBox="0 0 700 230" aria-hidden="true">
      <defs>
        <linearGradient id="bannerGradient" x1="0" y1="0" x2="0" y2="1">
          <stop offset="0" stop-color="#ff8a3a"/>
          <stop offset="0.35" stop-color="#ff5a1a"/>
          <stop offset="1" stop-color="#ff4d12"/>
        </linearGradient>
      </defs>
      <polygon points="0,0 700,0 700,151 350,229 0,151" fill="url(#bannerGradient)"/>
    </svg>

    <div class="firm-name">
      <span class="firm-name__main">MARCONA</span>
      <span class="firm-name__sub">LAW FIRM P.C.</span>
    </div>

    <h1 class="headline">CAR ACCIDENT?</h1>

    <div class="phone">
      <svg class="phone__icon" viewBox="0 0 64 64" aria-hidden="true">
        <path d="M14 10 l10 -3 l7 14 l-7 5 c3 8 8 14 15 18 l5 -7 l14 7 l-3 10 c-24 2 -44 -20 -41 -44 z"
              fill="none" stroke="#ffffff" stroke-width="4" stroke-linejoin="round"/>
        <path d="M36 14 a14 14 0 0 1 14 14" fill="none" stroke="#ff4d12" stroke-width="4" stroke-linecap="round"/>
        <path d="M38 4 a24 24 0 0 1 22 22" fill="none" stroke="#ff4d12" stroke-width="4" stroke-linecap="round"/>
      </svg>
      <span class="phone__number">(407) 555-0148</span>
    </div>

    <div class="slogan">
      <span class="slogan__lead">Don't Wait</span>
      <span class="slogan__action">Call Now</span>
    </div>
  </main>
</body>
</html>
```